Brookfarrow Osteopathy and dry needling business card

Business card for Brookfarrow Osteopathy and Dry Needling.

Industry/Entity Type

Health

Contact Information for Business Card

I do not have a phone number yet. I also do not have an email address yet. The physical address is: 48 Lower Crane Street Brookfarrow The website is: www.brookfarrowosteosteopathy.example My details are: Dr Martin Pellowe, Osteopath (B.Clin.Sci (Ost) M.Ost BSC ECON (Hons)

Colors
0094D4
00A9DD
6FCCEA
C7EBF8
E9F6FB

Requirements
Must have
• logo on the back
Nice to have
• Maybe a space for me to write an appointment time and date on the card.

```html
<!DOCTYPE html>
<html lang="en">
<head>
<meta charset="utf-8">
<title>Brookfarrow Osteopathy and Dry Needling – Business Card</title>
<link rel="stylesheet" href="https://fonts.googleapis.com/css2?family=Poppins:wght@400;500;700&display=swap">
<style>
  :root {
    --brand-blue: #0094D4;
    --brand-sky: #00A9DD;
    --accent-orange: #F39A2E;
    --paper: #FFFFFF;
    --backdrop: #E9F6FB;
    --card-w: 860px;
    --card-h: 491px;
  }
  * { box-sizing: border-box; margin: 0; padding: 0; }
  html, body {
    width: 1200px; height: 1200px; overflow: hidden;
    background: var(--backdrop);
    font-family: "Poppins", sans-serif;
  }
  .canvas {
    position: relative; width: 1200px; height: 1200px;
    display: flex; flex-direction: column; align-items: center; justify-content: center; gap: 60px;
  }
  .card {
    position: relative; width: var(--card-w); height: var(--card-h);
    overflow: hidden; box-shadow: 0 6px 20px rgba(0, 60, 100, 0.18);
  }

  /* Brand name block */
  .brand-mark {
    position: absolute; left: 0; right: 0;
    display: flex; align-items: center; justify-content: center; gap: 14px;
    font-weight: 500; white-space: nowrap;
  }
  .brand-dot {
    width: 40px; height: 40px; border-radius: 50%; flex: none;
    border: 2.5px solid currentColor;
  }
  .brand-name { font-size: 24px; line-height: 1.25; text-align: left; }

  /* Back */
  .card-back { background: var(--brand-blue); }
  .card-back .brand-mark { top: 84px; color: var(--paper); padding-left: 90px; }
  .appointment-box {
    position: absolute; left: 62px; right: 50px; top: 218px; height: 178px;
    background: var(--paper); border-radius: 14px;
  }
  .website {
    position: absolute; left: 0; right: 0; bottom: 38px; text-align: center;
    color: var(--paper); font-weight: 500; font-size: 22px; letter-spacing: 2px;
  }

  /* Front */
  .card-front { background: var(--paper); }
  .card-front .brand-mark { top: 108px; color: var(--brand-sky); }
  .person {
    position: absolute; left: 0; right: 0; top: 232px; text-align: center; color: var(--brand-sky);
  }
  .person-name { font-weight: 700; font-size: 30px; letter-spacing: 1px; text-transform: uppercase; line-height: 1.3; }
  .person-title { font-weight: 400; font-size: 20px; margin-top: 4px; }
  .contact {
    position: absolute; left: 0; right: 0; top: 360px; list-style: none;
    display: flex; flex-direction: column; align-items: center;
    color: var(--brand-sky); font-size: 20px; line-height: 1.35;
  }
  .contact-label { color: var(--accent-orange); font-weight: 500; margin-right: 6px; }
  .edge-stripes { position: absolute; left: 0; right: 0; bottom: 0; }
  .stripe-orange { height: 5px; background: var(--accent-orange); }
  .stripe-gap { height: 3px; background: var(--paper); }
  .stripe-blue { height: 14px; background: var(--brand-blue); }
</style>
</head>
<body>
  <main class="canvas">
    <section class="card card-back" aria-label="Card back">
      <div class="brand-mark">
        <span class="brand-dot"></span>
        <span class="brand-name">Brookfarrow Osteopathy<br>&amp; Dry Needling</span>
      </div>
      <div class="appointment-box" aria-label="Space to write appointment date and time"></div>
      <p class="website">www.brookfarrowosteosteopathy.example</p>
    </section>

    <section class="card card-front" aria-label="Card front">
      <div class="brand-mark">
        <span class="brand-dot"></span>
        <span class="brand-name">Brookfarrow Osteopathy<br>&amp; Dry Needling</span>
      </div>
      <div class="person">
        <h1 class="person-name">Dr Martin Pellowe</h1>
        <p class="person-title">Osteopath (B.Clin.Sci (Ost) M.Ost BSC ECON (Hons)</p>
      </div>
      <ul class="contact">
        <li><span class="contact-label">A:</span>48 Lower Crane Street, Brookfarrow</li>
      </ul>
      <div class="edge-stripes">
        <div class="stripe-orange"></div>
        <div class="stripe-gap"></div>
        <div class="stripe-blue"></div>
      </div>
    </section>
  </main>
</body>
</html>
```